New website for our Escape Room

We are wanting to create a new website for our website. We have 2 different locations that guests will choose their location on the home page. Then we have 5 different escape room experiences. We like clean and fresh but fun. Our logo is black white and red. We like a modern feel that is simple to navigate. I love movement on the page. You can see our current site at lockwickpuzzlehall.example
We like fresh and modern. It needs to include much of the same information as out current site but we won't like the look of our site.

Target Market(s)

amusement, escape rooms.

Industry/Entity Type

escape room

Number of Pages Required

4 page

Requirements
Must have
• info on all 4 escape rooms, option to choose between Cedar Hollow and Riverton locations.

```html
<!DOCTYPE html>
<html lang="en">
<head>
<meta charset="utf-8">
<title>Lockwick Puzzle Hall – Escape Rooms</title>
<link rel="stylesheet" href="https://fonts.googleapis.com/css2?family=Oswald:wght@400;500;600&family=Roboto+Condensed:wght@400;700&family=Mulish:wght@400;700;800&display=swap">
<style>
:root{
  --red:#ff0000;
  --red-deep:#c40000;
  --black:#000000;
  --white:#ffffff;
  --line:#444444;
}
*{margin:0;padding:0;box-sizing:border-box}
html,body{width:1200px;height:3044px;overflow:hidden;background:var(--black);color:var(--white)}
body{position:relative;font-family:'Mulish',sans-serif}
.abs{position:absolute}
.cond{font-family:'Oswald',sans-serif;text-transform:uppercase}

/* header */
.site-header{position:absolute;left:0;top:0;width:1200px;height:100px;background:var(--black)}
.brand{position:absolute;left:131px;top:18px;height:58px;font-family:'Oswald',sans-serif;font-weight:500;font-size:52px;line-height:58px;letter-spacing:1px;color:var(--white)}
.locations{position:absolute;top:17px;right:132px;display:flex;gap:12px}
.locations a{display:block;border:2px solid var(--red);color:var(--red);font-family:'Oswald',sans-serif;font-size:16px;padding:2px 10px;text-decoration:none;text-transform:uppercase}
.main-nav{position:absolute;top:62px;right:132px;display:flex;gap:29px}
.main-nav a{font-family:'Oswald',sans-serif;font-size:16px;color:var(--white);text-decoration:none;text-transform:uppercase}
.main-nav a.active{color:var(--red);border-bottom:2px solid var(--red);padding-bottom:2px}

/* hero */
.hero{position:absolute;left:0;top:100px;width:1200px;height:500px;border-bottom:2px solid var(--red);
  background:linear-gradient(90deg,#3b3a30 0%,#5a4a36 25%,#6b6a66 50%,#4a4c45 75%,#2c2e2a 100%)}
.hero::after{content:"";position:absolute;inset:0;background:radial-gradient(ellipse at center,rgba(0,0,0,.1),rgba(0,0,0,.45))}
.hero-content{position:absolute;left:0;top:145px;width:1200px;text-align:center;z-index:1}
.hero h1{font-family:'Oswald',sans-serif;font-weight:600;font-size:66px;line-height:80px;text-transform:uppercase}
.hero p{font-family:'Oswald',sans-serif;font-size:25px;margin-top:6px;text-transform:uppercase}
.btn-outline-red{display:inline-block;margin-top:18px;background:var(--red);border:2px solid var(--white);padding:9px 18px;font-weight:800;font-size:15px;text-transform:uppercase}
.dots{position:absolute;bottom:26px;left:0;width:1200px;display:flex;justify-content:center;gap:7px;z-index:1}
.dots span{width:8px;height:8px;background:var(--white)}
.dots span.on{background:var(--red);outline:2px solid var(--white)}

/* rooms */
.rooms-title{position:absolute;left:0;width:1200px;top:650px;text-align:center;font-family:'Oswald',sans-serif;font-weight:500;font-size:23px;line-height:34px;text-transform:uppercase}
.room-card{position:absolute;width:459px;height:206px;border:1px solid var(--red);background:var(--black)}
.room-card.featured{background:var(--red)}
.room-icon{position:absolute;left:28px;top:40px;width:110px;height:110px;border:2px solid var(--red);border-radius:6px}
.room-card.featured .room-icon{border-color:var(--white)}
.room-body{position:absolute;left:168px;top:36px;width:255px}
.room-body h3{font-family:'Oswald',sans-serif;font-weight:500;font-size:18px;text-transform:uppercase;margin-bottom:8px}
.room-body p{font-size:12px;line-height:17px;height:51px;overflow:hidden}
.room-btn{display:inline-block;margin-top:14px;margin-left:3px;background:var(--red);color:var(--white);font-weight:800;font-size:10.5px;padding:6px 13px;text-transform:uppercase}
.room-card.featured .room-btn{background:var(--white);color:var(--red)}

/* welcome */
.welcome-eyebrow{left:195px;top:1372px;font-size:24px;font-weight:500}
.welcome-name{left:193px;top:1396px;font-size:52px;font-weight:600;color:var(--red)}
.photo{position:absolute}
.welcome-copy{left:612px;top:1370px;width:430px;font-size:13.5px;line-height:19.5px}
.welcome-copy p+p{margin-top:19px}
.btn-small{position:absolute;background:var(--red);color:var(--white);font-weight:800;font-size:11px;padding:7px 13px;text-transform:uppercase;border:1px solid #ff5a5a}

/* benefits */
.benefits-title{position:absolute;left:0;width:1200px;top:1790px;text-align:center;font-family:'Roboto Condensed',sans-serif;font-weight:700;font-size:32px;line-height:54px;text-transform:uppercase}
.benefit{position:absolute;top:1890px;width:218px;height:305px;text-align:center}
.benefit .kicker{position:absolute;left:0;width:100%;top:116px;font-family:'Oswald',sans-serif;font-size:17px;color:var(--red);text-transform:uppercase;opacity:.8}
.benefit h4{position:absolute;left:10px;width:198px;top:146px;font-family:'Roboto Condensed',sans-serif;font-weight:700;font-size:18px;line-height:24px;text-transform:uppercase}
.benefit.active .kicker{top:93px;color:var(--white);opacity:1}
.benefit.active h4{top:121px}
.benefit.active .plus{position:absolute;left:100px;top:204px;width:20px;height:20px;border-radius:50%;background:var(--white);color:var(--red);font-size:15px;line-height:19px;font-weight:800}

/* who */
.who{position:absolute;left:0;top:2270px;width:1200px;height:560px;background:radial-gradient(ellipse at 45% 45%,#161616,#050505 75%)}
.who-ghost{position:absolute;left:0;width:1200px;top:2278px;text-align:center;font-family:'Roboto Condensed',sans-serif;font-weight:700;font-size:78px;color:transparent;-webkit-text-stroke:1px #2a2a2a;text-transform:uppercase;letter-spacing:1px}
.who-title{position:absolute;left:0;width:1200px;top:2295px;text-align:center;font-family:'Roboto Condensed',sans-serif;font-weight:700;font-size:32px;text-transform:uppercase}
.who-copy{position:absolute;left:144px;top:2390px;width:408px;font-family:'Roboto Condensed',sans-serif;font-size:14px;line-height:29px;text-align:justify}
.who-list{position:absolute;left:144px;top:2547px;width:330px;display:grid;grid-template-columns:160px 170px;row-gap:18px;font-family:'Roboto Condensed',sans-serif;font-size:15px;color:var(--red)}
.who-list li{list-style:none;display:flex;align-items:center;gap:6px}
.who-list i{width:14px;height:14px;border:2px solid var(--red);border-radius:50%;position:relative}
.who-list i::after{content:"";position:absolute;left:3px;top:3px;width:4px;height:4px;border-radius:50%;background:var(--red)}
.btn-learn{position:absolute;left:144px;top:2639px;width:124px;height:52px;background:var(--red);font-family:'Roboto Condensed',sans-serif;font-size:19px;line-height:52px;text-align:center}

/* footer */
.follow{position:absolute;right:283px;top:2868px;font-family:'Oswald',sans-serif;font-size:14px;line-height:20px}
.social{position:absolute;top:2862px;display:flex;gap:16px;right:135px}
.social span{width:32px;height:32px;border-radius:50%;background:var(--red)}
.footer-nav{position:absolute;right:135px;top:2915px;font-family:'Oswald',sans-serif;font-size:14px;display:flex;gap:10px}
.footer-rule{position:absolute;left:131px;top:2958px;width:936px;height:1px;background:var(--line)}
.copyright{position:absolute;left:0;width:1200px;top:2994px;text-align:center;font-size:11px}
</style>
</head>
<body>

<header class="site-header">
  <div class="brand">LOCKWICK</div>
  <nav class="locations"><a>Cedar Hollow</a><a>Riverton</a></nav>
  <nav class="main-nav">
    <a class="active">Home</a><a>About Us</a><a>Escape Rooms</a><a>FAQ</a><a>Gallery</a><a>Gift Cards</a><a>Contact</a>
  </nav>
</header>

<section class="hero" role="img" aria-label="Photo of an open steel cell door in a long brick prison corridor">
  <div class="hero-content">
    <h1>Iron Block</h1>
    <p>Can you break out before the lights go down?</p>
    <span class="btn-outline-red">Read More</span>
  </div>
  <div class="dots"><span></span><span></span><span class="on"></span><span></span><span></span></div>
</section>

<h2 class="rooms-title">Find the right room for you</h2>
<div class="abs" style="left:581px;top:697px;width:32px;height:2px;background:var(--red)"></div>

<article class="room-card featured" style="left:131px;top:753px">
  <div class="room-icon" role="img" aria-label="Line icon of a prison on a rocky island"></div>
  <div class="room-body">
    <h3>Iron Block</h3>
    <p>The Iron Block was raised on a cold island to hold the most cunning and feared prisoners of its age.</p>
    <span class="room-btn">Read More</span>
  </div>
</article>
<article class="room-card" style="left:608px;top:753px">
  <div class="room-icon" role="img" aria-label="Line icon of a spiked bat and a crate"></div>
  <div class="room-body">
    <h3>Last Outbreak</h3>
    <p>Relax, the world isn't truly ending, but our Last Outbreak room will push your team's sharpest reasoning to its limit,</p>
    <span class="room-btn">Read More</span>
  </div>
</article>
<article class="room-card" style="left:131px;top:981px">
  <div class="room-icon" role="img" aria-label="Line icon of a restraint chair with lightning"></div>
  <div class="room-body">
    <h3>Ward Nine</h3>
    <p>Whether you've pictured life as an agent, a night locked inside a ward, or putting dark figures behind bars, you're bound</p>
    <span class="room-btn">Read More</span>
  </div>
</article>
<article class="room-card" style="left:608px;top:981px">
  <div class="room-icon" role="img" aria-label="Line icon of a small cabin house"></div>
  <div class="room-body">
    <h3>Hollow Lodge</h3>
    <p>Old man Harlan passed on many years ago, yet he never really left — far from it! Each hour his spirit returns to guard the</p>
    <span class="room-btn">Read More</span>
  </div>
</article>

<svg class="abs" style="left:0;top:1225px" width="1200" height="565" viewBox="0 1225 1200 565" aria-hidden="true">
  <polygon fill="#ff0000" points="0,1255 290,1283 600,1318 1200,1225 1200,1258 615,1318 0,1320"/>
  <polygon fill="#ff0000" points="0,1255 28,1298 28,1740 290,1746 0,1780"/>
  <polygon fill="#000" points="28,1298 290,1284 600,1318 28,1320"/>
  <polygon fill="#6a0000" opacity=".6" points="290,1283 600,1318 560,1318 330,1292"/>
</svg>
<div class="abs" style="left:49px;top:1510px;width:18px;height:18px;border-radius:50%;background:var(--white)"></div>

<div class="abs cond welcome-eyebrow">Welcome to</div>
<div class="abs cond welcome-name">LOCKWICK</div>
<div class="photo" role="img" aria-label="Photo of hands gripping a gap in old wooden doors" style="left:199px;top:1486px;width:180px;height:180px;background:linear-gradient(90deg,#1e1712,#3a2c22 45%,#2a201a 55%,#15100c)"></div>
<div class="photo" role="img" aria-label="Photo of a dark cell with a barred window and a ball and chain" style="left:420px;top:1470px;width:141px;height:141px;background:radial-gradient(ellipse at 50% 30%,#4a5560,#1a1f24 70%,#0c0e10)"></div>
<div class="abs welcome-copy">
  <p>Lockwick Puzzle Hall is the pulse-racing, lock-picking, brain-twisting beat-the-clock challenge that Riverton and Cedar Hollow have been hoping for. With five distinct rooms to pick from, our games bring a thrill of discovery you rarely feel after childhood. Be warned, though: our rooms are not for the easily rattled.</p>
  <p>Everything we run is safe and friendly, but since several of our rooms lean into spooky themes, some guests find them frightening. The moment the door closes, you are locked in, and any player who walks out early removes the whole team's time from the scoreboard.</p>
</div>
<span class="btn-small" style="left:618px;top:1636px">Read More</span>

<h2 class="benefits-title">Discover the benefits of escape rooms</h2>

<div class="benefit" role="img" aria-label="Photo of a figure standing in a stone maze" style="left:131px;background:linear-gradient(180deg,#3a3d42,#23262a 60%,#141517)">
  <span class="kicker">Improve</span><h4>Communication and social skills</h4>
</div>
<div class="benefit active" style="left:370px;background:radial-gradient(ellipse at 40% 50%,#ff1a1a,#e00000)">
  <span class="kicker">Challenge your</span><h4>Creative thinking and problem-solving skills</h4><span class="plus">+</span>
</div>
<div class="benefit" role="img" aria-label="Photo of hands over a vintage map with a dagger" style="left:611px;background:linear-gradient(160deg,#3a3530,#5a3a28 50%,#2a1a14)">
  <span class="kicker">Enhance and</span><h4>Build your memory</h4>
</div>
<div class="benefit" role="img" aria-label="Photo of a key on a tag lying on wooden boards" style="left:851px;background:linear-gradient(160deg,#6a5a48,#4a3a28 55%,#2a1e14)">
  <span class="kicker">Improve</span><h4>Your mood</h4>
</div>

<section class="who" role="img" aria-label="Dim photo of an old mansion hall"></section>
<div class="who-ghost">Lockwick Who</div>
<h2 class="who-title">Lockwick Who</h2>
<p class="who-copy">Lockwick Puzzle Hall is the pulse-racing, lock-picking, brain-twisting beat-the-clock challenge that Riverton and Cedar Hollow have been hoping for. With five distinct rooms to pick from, our games bring a thrill of discovery you rarely feel after childhood.</p>
<ul class="who-list">
  <li><i></i>Gamers</li><li><i></i>Friends &amp; Family</li>
  <li><i></i>Team Building</li><li><i></i>Tourists &amp; Visitors</li>
</ul>
<span class="btn-learn">Learn More</span>

<svg class="abs" style="left:614px;top:2385px" width="442" height="315" viewBox="0 0 442 315" aria-hidden="true">
  <polygon fill="#ff0000" points="0,0 180,18 442,0 442,315 180,295 0,315"/>
  <polygon fill="#000" points="20,22 421,22 421,295 20,295"/>
</svg>
<div class="photo" role="img" aria-label="Photo of a dark room with a tall window and a checkered floor" style="left:634px;top:2408px;width:401px;height:271px;background:linear-gradient(180deg,#1a1a1a,#3a3a3a 45%,#222 70%,#111)"></div>

<svg class="abs" style="left:0;top:2745px" width="1200" height="100" viewBox="0 0 1200 100" aria-hidden="true">
  <polygon fill="#ff0000" points="0,5 600,95 1200,50 1200,58 600,98 0,30"/>
  <polygon fill="#7a0000" points="600,95 900,70 880,76 600,98"/>
</svg>

<footer>
  <div class="brand" style="top:2868px;left:134px;font-size:56px;line-height:62px;height:62px">LOCKWICK</div>
  <span class="follow cond">Follow us</span>
  <div class="social" aria-label="Social links">
    <span role="img" aria-label="Social profile one"></span>
    <span role="img" aria-label="Social profile two"></span>
    <span role="img" aria-label="Social profile three"></span>
  </div>
  <nav class="footer-nav cond">
    <span>Home</span><span>|</span><span>FAQs</span><span>|</span><span>Blog</span><span>|</span><span>Gift Cards</span><span>|</span><span>Contact</span><span>|</span><span>Privacy Policy</span>
  </nav>
  <div class="footer-rule"></div>
  <p class="copyright">Copyright © 2022 All Rights Reserved</p>
</footer>

</body>
</html>
```